VORLANE (PTY)LTD Website design

WEBSITE design based on our different divisions in our organization.
Our company specializes in the following.
Construction
Property development
Demolition
Mining
Transport
Manufacturing of concrete bricks and blocks
Lightweight concrete Readymix
I want a very modern website and look that fits in with our organization and the changing times of the world.
The website must be very professional and crisp and should appeal to both the younger generation and older generation of business leaders and.
The website must be very user friendly and easy to navigate, simple yet modern, professional and corporate.

```html
<!DOCTYPE html>
<html lang="en">
<head>
<meta charset="utf-8">
<title>VORLANE (PTY)LTD</title>
<link rel="stylesheet" href="https://fonts.googleapis.com/css2?family=Ubuntu:ital,wght@0,400;0,500;0,700;1,500;1,700&display=swap">
<style>
  :root {
    --brand-blue: #33a5d6;
    --card-blue: #0891cd;
    --brand-navy: #1a6fb0;
    --ink: #111111;
    --white: #ffffff;
    --quote-tint: rgba(255,255,255,0.22);
  }
  * { box-sizing: border-box; margin: 0; padding: 0; }
  html, body { width: 1200px; height: 973px; overflow: hidden; }
  body { font-family: "Ubuntu", sans-serif; background: var(--white); position: relative; }

  .site-header { height: 62px; display: flex; align-items: center; justify-content: center; }
  .brand-name { font-size: 34px; font-weight: 700; color: var(--brand-navy); letter-spacing: 1px; }

  .main-nav { height: 45px; background: var(--brand-blue); border: 1px solid #2a8fc0; display: flex; align-items: center; padding-left: 29px; }
  .main-nav a { color: var(--white); text-decoration: none; font-size: 15px; font-weight: 500; margin-right: 57px; }

  .hero { position: relative; height: 347px; overflow: hidden; }
  .hero-photo { position: absolute; inset: 0; background:
      linear-gradient(180deg, #b9b4cc 0%, #c9a5b2 20%, #6c6f86 45%, #5b5b68 70%, #4a4440 100%); }
  .hero-content { position: relative; text-align: center; color: var(--white); padding-top: 60px; }
  .hero-title { font-size: 58px; font-weight: 700; line-height: 66px; letter-spacing: -1px; }
  .hero-text { font-size: 22px; line-height: 35px; margin: 47px 30px 0; }

  .testimonials { padding: 0 38px; }
  .section-title { text-align: center; font-size: 31px; font-weight: 700; color: var(--ink); line-height: 1; padding: 24px 0 22px; }
  .testimonial-card { position: relative; height: 114px; background: var(--card-blue); margin-bottom: 15px; color: var(--white); padding: 24px 0 0 47px; box-shadow: 0 1px 3px rgba(0,0,0,0.2); overflow: hidden; }
  .testimonial-quote { font-size: 21px; line-height: 28px; }
  .testimonial-author { font-size: 16px; font-weight: 700; font-style: italic; margin-top: 7px; opacity: 0.85; }
  .quote-mark { position: absolute; right: 20px; bottom: -40px; font-size: 100px; font-weight: 700; font-style: italic; color: var(--quote-tint); line-height: 1; }

  .site-footer { position: absolute; left: 0; right: 0; bottom: 0; height: 55px; background: var(--brand-blue); color: var(--white); font-size: 15px; display: flex; align-items: center; padding-left: 19px; }
</style>
</head>
<body>
  <header class="site-header">
    <span class="brand-name">VORLANE</span>
  </header>

  <nav class="main-nav">
    <a href="#">Home</a>
    <a href="#">About</a>
    <a href="#">Services</a>
    <a href="#">Contact</a>
  </nav>

  <section class="hero">
    <div class="hero-photo" role="img" aria-label="Photo of a two-storey family house with garage at dusk under a pink sky"></div>
    <div class="hero-content">
      <h1 class="hero-title">VORLANE</h1>
      <p class="hero-text">From construction and property development to demolition, mining and transport, VORLANE delivers complete solutions under one roof. Our plants manufacture concrete bricks and blocks and supply lightweight concrete readymix, giving every client one trusted partner from the first site survey to the final handover.</p>
    </div>
  </section>

  <section class="testimonials">
    <h2 class="section-title">TESTIMONIAL</h2>
    <article class="testimonial-card">
      <p class="testimonial-quote">Their construction and property development team delivered on time.</p>
      <p class="testimonial-author">John Doe</p>
      <span class="quote-mark">”</span>
    </article>
    <article class="testimonial-card">
      <p class="testimonial-quote">Reliable demolition, mining and transport support on every site.</p>
      <p class="testimonial-author">Jane Doe</p>
      <span class="quote-mark">”</span>
    </article>
    <article class="testimonial-card">
      <p class="testimonial-quote">Quality concrete bricks, blocks and lightweight readymix every time.</p>
      <p class="testimonial-author">Richard Roe</p>
      <span class="quote-mark">”</span>
    </article>
  </section>

  <footer class="site-footer">Copyright © 2018 VORLANE.</footer>
</body>
</html>
```